Corbett Architecture (business card)

We need a business card design. We are a full service architectural firm that specializes in mostly residential projects and some commercial projects. We are located in Hudson Valley, New York. We work with high end clients and want a business card that is memorable and has a sleek, modern, design but will not go out of style (timeless).

Target Market(s)

high end residential clients

Industry/Entity Type

Architect

Contact Information for Business Card

Front of card
Company Logo
website: www.corbettdesignstudo.example
what we do: residential, Commercial

back of card
Owner's Name: Martin Corbett
owner's title: Principal
Business address: 2867 Orchard Lane Suite B, Maplethorpe, NY 10938
phone number: 845-555-0192
e-mail: mc@corbettdesignstudio.example

We like:
icons
sleek and clean design
simple not too busy or too much text

Font styles to use
Sans Serif

Colors
0356a4

Requirements
Must have
• company colors are navy blue, white, and gray
• Front of card
• Company Logo
• website: www.corbettdesignstudo.example
• what we do: residential, Commercial
• back of card
• Owner's Name: Martin Corbett
• owner's title: Principal
• Business address: 2867 Orchard Lane Suite B, Maplethorpe, NY 10938
• phone number: 845-555-0192
• e-mail: mc@corbettdesignstudio.example
Nice to have
• We like:
• icons
• sleek and clean design
• simple not too much text
• color of the card to be either blue or gray
Should not have
• we do not like houses in the design or plans of houses-this is over done and we don't like it.
• no QR CODES

```html
<!DOCTYPE html>
<html lang="en">
<head>
<meta charset="utf-8">
<title>Corbett Architecture — Business Card</title>
<link rel="stylesheet" href="https://fonts.googleapis.com/css2?family=Montserrat:wght@400;500&family=Roboto:wght@400;500;700&display=swap">
<style>
  :root {
    --navy: #2a2766;
    --navy-deep: #201d55;
    --white: #ffffff;
    --gray: #5f6066;
    --gray-light: #8a8b90;
    --rule: #6b6c70;
    --backdrop: #2b2b2e;
  }
  * { box-sizing: border-box; margin: 0; padding: 0; }
  html, body {
    width: 1200px;
    height: 864px;
    overflow: hidden;
    background: var(--backdrop);
  }
  .canvas {
    position: relative;
    width: 1200px;
    height: 864px;
  }
  .card {
    position: absolute;
    width: 640px;
    height: 366px;
    border-radius: 4px;
    box-shadow: 0 14px 30px rgba(0,0,0,0.45);
    overflow: hidden;
  }

  /* Front */
  .card-front {
    left: 180px;
    top: 46px;
    background: var(--navy);
    color: var(--white);
  }
  .front-brand {
    position: absolute;
    left: 120px;
    top: 126px;
    display: flex;
    align-items: center;
    gap: 18px;
  }
  .brand-square {
    width: 52px;
    height: 52px;
    background: currentColor;
  }
  .brand-name {
    font-family: "Montserrat", sans-serif;
    font-weight: 400;
    text-transform: uppercase;
    letter-spacing: 2px;
    line-height: 1.05;
    font-size: 30px;
  }
  .brand-name .suffix { font-size: 16px; letter-spacing: 1.5px; }
  .services {
    position: absolute;
    left: 0;
    right: 0;
    top: 262px;
    display: flex;
    justify-content: center;
    gap: 16px;
    font-family: "Roboto", sans-serif;
    font-size: 16px;
    letter-spacing: 0.5px;
  }
  .services li {
    list-style: none;
    display: flex;
    align-items: center;
    gap: 5px;
  }
  .services li::before {
    content: "";
    width: 8px;
    height: 8px;
    border-radius: 50%;
    background: var(--white);
  }

  /* Back */
  .card-back {
    left: 380px;
    top: 452px;
    background: var(--white);
    color: var(--gray);
  }
  .back-brand {
    position: absolute;
    left: 56px;
    top: 44px;
    display: flex;
    align-items: center;
    gap: 12px;
    color: var(--gray);
  }
  .back-brand .brand-square {
    width: 36px;
    height: 36px;
    background: var(--navy);
  }
  .back-brand .brand-name { font-size: 21px; letter-spacing: 1.6px; }
  .back-brand .brand-name .suffix { font-size: 12px; }
  .top-rule {
    position: absolute;
    left: 300px;
    right: 40px;
    top: 146px;
    height: 1.5px;
    background: var(--rule);
  }
  .edge-tab {
    position: absolute;
    left: 0;
    top: 214px;
    width: 22px;
    height: 34px;
    background: var(--navy);
  }
  .person {
    position: absolute;
    left: 56px;
    top: 196px;
    right: 40px;
    font-family: "Roboto", sans-serif;
  }
  .person-name {
    color: var(--navy);
    font-weight: 700;
    font-size: 21px;
    letter-spacing: 0.3px;
    text-transform: uppercase;
  }
  .person-title {
    display: flex;
    align-items: center;
    gap: 10px;
    font-weight: 700;
    font-size: 17px;
    color: var(--gray);
  }
  .person-title::after {
    content: "";
    flex: 1;
    height: 1.5px;
    background: var(--rule);
  }
  .contacts {
    position: absolute;
    left: 64px;
    top: 262px;
    font-family: "Roboto", sans-serif;
    font-size: 17px;
    line-height: 26px;
    color: var(--gray);
    list-style: none;
  }
  .contacts li { display: flex; align-items: center; gap: 10px; }
  .contacts svg { width: 16px; height: 16px; fill: var(--navy); flex: none; }
  .contacts .site-strong { color: var(--navy); font-weight: 500; }
  .address {
    position: absolute;
    right: 40px;
    top: 178px;
    text-align: right;
    font-family: "Roboto", sans-serif;
    font-size: 17px;
    line-height: 24px;
    color: var(--gray);
    font-style: normal;
  }
</style>
</head>
<body>
<main class="canvas">

  <section class="card card-front" aria-label="Card front">
    <div class="front-brand">
      <span class="brand-square" aria-hidden="true"></span>
      <p class="brand-name">Corbett<br>Architecture <span class="suffix">PLLC</span></p>
    </div>
    <ul class="services">
      <li>Residential</li>
      <li>Commercial</li>
    </ul>
  </section>

  <section class="card card-back" aria-label="Card back">
    <div class="back-brand">
      <span class="brand-square" aria-hidden="true"></span>
      <p class="brand-name">Corbett<br>Architecture <span class="suffix">PLLC</span></p>
    </div>
    <span class="top-rule" aria-hidden="true"></span>
    <span class="edge-tab" aria-hidden="true"></span>

    <div class="person">
      <p class="person-name">Martin Corbett</p>
      <p class="person-title">Principal</p>
    </div>

    <address class="address">2867 Orchard Lane Suite B,<br>Maplethorpe, NY 10938</address>

    <ul class="contacts">
      <li>
        <svg viewBox="0 0 16 16" aria-hidden="true"><path d="M3 2h3l1.5 3.5-2 1.2a8 8 0 0 0 3.8 3.8l1.2-2L14 10v3a1 1 0 0 1-1 1A11 11 0 0 1 2 3a1 1 0 0 1 1-1z"/></svg>
        845-555-0192
      </li>
      <li>
        <svg viewBox="0 0 16 16" aria-hidden="true"><path d="M1 3h14v10H1z M2 4.2v.3l6 4 6-4v-.3z" fill-rule="evenodd"/></svg>
        mc@corbettdesignstudio.example
      </li>
      <li>
        <svg viewBox="0 0 16 16" aria-hidden="true"><path fill="none" stroke="currentColor" d="M8 1.5a6.5 6.5 0 1 0 0 13a6.5 6.5 0 1 0 0-13zM1.5 8h13M8 1.5c-3 3.5-3 9.5 0 13M8 1.5c3 3.5 3 9.5 0 13" style="stroke:var(--navy)"/></svg>
        <span>www.<span class="site-strong">corbettdesignstudo</span>.example</span>
      </li>
    </ul>
  </section>

</main>
</body>
</html>
```